Letterhead Design Project

Consulting Company , we want a letterhead incorporating both the picture provided and the logo provided. The font name is monotype corsiva.
Target Market(s)
Dentist
Industry/Entity Type
Consulting
Font styles to use
Other font styles liked:
- monotype corsiva

Colors
0455a3
Requirements
Must have
- the logo, the picture (see attached), the website name, the email. and the phone numbers.
- Website: www.trquillarisadvisory.solutions
- Email: will be provided to the winner, please use placeholder
- Phone numbers:
- Petra Hallum 5829017763
- Owen Vrastik 6148250397

Nice to have
- a swoop or wave across the bottom. a line up the side. I don't know guys. design something unique and professional.

Should not have
- arrows pointing off the logo or anywhere. no arrows. our logo altered in anyway. no broken circles. no variences in blue. we like our logo the way it is. the font is monotype corsiva

```html
<!DOCTYPE html>
<html lang="en">
<head>
<meta charset="utf-8">
<title>Trquillaris Advisory Letterhead</title>
<link href="https://fonts.googleapis.com/css2?family=Open+Sans:wght@300;400;600&display=swap" rel="stylesheet">
<style>
  :root {
    --brand-blue: #0455a3;
    --ink: #333333;
    --ink-dark: #222222;
    --soft-band: #e1e4f3;
    --paper: #ffffff;
    --photo-tone: #9a9a9a;
  }
  * { margin: 0; padding: 0; box-sizing: border-box; }
  html, body { width: 849px; height: 1200px; overflow: hidden; background: var(--paper); }
  body { font-family: "Open Sans", Arial, sans-serif; color: var(--ink); }
  .letterhead { position: relative; width: 849px; height: 1200px; overflow: hidden; }
  .abs { position: absolute; }

  .brand-mark { left: 46px; top: 69px; width: 74px; height: 74px; border: 5px solid var(--brand-blue); border-radius: 50%; }
  .brand-name { left: 128px; top: 97px; font-size: 16px; font-weight: 600; color: var(--brand-blue); white-space: nowrap; }

  .portrait { left: 498px; top: 31px; width: 94px; height: 94px; border-radius: 50%; border: 3px solid var(--brand-blue); background: radial-gradient(circle at 50% 40%, #c9c9c9, var(--photo-tone) 60%, #3a3a3a); }
  .signer-name { left: 470px; top: 138px; width: 150px; text-align: center; font-size: 15px; font-weight: 600; color: var(--brand-blue); }
  .signer-title { left: 470px; top: 155px; width: 150px; text-align: center; font-size: 11px; color: var(--ink-dark); }

  .contacts { left: 634px; top: 28px; font-size: 11.5px; line-height: 15px; color: var(--ink-dark); letter-spacing: 0.3px; }
  .contacts .label { font-weight: 600; }
  .contacts .person { color: var(--brand-blue); font-size: 13.5px; letter-spacing: 0; margin-top: 4px; line-height: 18px; }
  .contacts .email { margin-top: 10px; letter-spacing: -0.5px; }

  .rule { height: 7px; background: var(--brand-blue); }
  .rule-left { left: 0; top: 197px; width: 538px; border-radius: 0 4px 4px 0; }
  .rule-right { left: 763px; top: 197px; width: 86px; border-radius: 4px 0 0 4px; }
  .website { left: 550px; top: 191px; font-size: 12.5px; letter-spacing: -0.6px; color: var(--ink-dark); }
  .website span { color: var(--brand-blue); }

  .recipient { left: 77px; top: 315px; font-size: 20px; font-weight: 300; line-height: 32px; }
  .recipient .to-name { font-size: 22px; font-weight: 600; color: var(--brand-blue); }
  .salutation { left: 77px; top: 443px; font-size: 21px; font-weight: 300; }
  .body-copy { left: 77px; width: 710px; font-size: 18.8px; font-weight: 300; line-height: 32.2px; }
  .para-one { top: 514px; }
  .para-two { top: 739px; }

  .closing { left: 77px; top: 1038px; font-size: 15px; font-weight: 300; line-height: 25px; }
  .closing .sign { font-size: 17px; font-weight: 600; color: var(--brand-blue); }

  .wave-bar { height: 15px; background: var(--soft-band); border-radius: 8px 0 0 8px; right: 0; }
  .bar-one { left: 435px; top: 1098px; }
  .bar-two { left: 282px; top: 1130px; }
  .bar-three { left: 77px; top: 1161px; }
  .footer-rule { left: 0; top: 1193px; width: 849px; height: 7px; background: var(--brand-blue); }
</style>
</head>
<body>
<div class="letterhead">
  <header>
    <div class="abs brand-mark"></div>
    <div class="abs brand-name">Trquillaris Advisory, LLC</div>

    <div class="abs portrait" role="img" aria-label="Portrait photo of Petra Hallum, President"></div>
    <div class="abs signer-name">Petra Hallum</div>
    <div class="abs signer-title">President</div>

    <div class="abs contacts">
      <div><span class="label">A:</span> 418 Larkfield Lane</div>
      <div>Brookhaven Falls, Kentucky 40399</div>
      <div class="person">Petra Hallum</div>
      <div><span class="label">T:</span> 5829017763</div>
      <div class="person">Owen Vrastik</div>
      <div><span class="label">T:</span> 6148250397</div>
      <div class="email"><span class="label">E:</span> placeholder@placeholder.solutions</div>
    </div>

    <div class="abs rule rule-left"></div>
    <div class="abs website">www.<span>trquillaris</span>advisory.solutions</div>
    <div class="abs rule rule-right"></div>
  </header>

  <main>
    <div class="abs recipient">
      <div>To</div>
      <div class="to-name">Marten Coyle</div>
      <div>Director</div>
    </div>
    <div class="abs salutation">Dear Sir,</div>
    <p class="abs body-copy para-one">Sed ut perspiciatis, unde omnis iste natus error sit voluptatem accusa tium dolorem antium, totam rem aperiam eaque ipsa, quae ab illo inventore veri tatis et quasi architecto beatae vitae dicta sunt, explicabo. Nemo enim ipsam voluptatem, quia voluptas voluptatem sequi nesciunt, neque porro quisquam est, qui dolorem ipsum, quia dolor sit sit, aspernatur aut odit aut fugit, sed quia consequuntur magni dolores eos, qui ration.</p>
    <p class="abs body-copy para-two">Sed ut perspiciatis, unde omnis iste natus error sit voluptatem accusantium dolorem antium, totam rem aperiam eaque ipsa, quae ab illo inventore veritatis et quasi architecto beatae vitae dicta sunt, explicabo. Sed ut perspiciatis unde omnis iste natus error sit voluptatem accusantium doloremque laudantium, totam rem aperiam, eaque ipsa quae ab illo inventore veritatis et quasi architecto beatae vitae dicta sunt explicabo.</p>
    <div class="abs closing">
      <div>Sincerely,</div>
      <div class="sign">Petra Hallum</div>
    </div>
  </main>

  <footer>
    <div class="abs wave-bar bar-one"></div>
    <div class="abs wave-bar bar-two"></div>
    <div class="abs wave-bar bar-three"></div>
    <div class="abs footer-rule"></div>
  </footer>
</div>
</body>
</html>
```